Tidewell Estates Agency Guarantee

We need a flyer to promote a Sydney based property management agency.
We specialise in Property Management on the Northern Beaches of Sydney. A small boutique agency that prides itself on high quality customer service and the lowest fees.
We would like this flyer to promote our listed features in the document provided and focus on our money back guarantee.
The flyer must:
- be designed to match our website www.tidewellestatesagency.com.au
- Contain our logo and contact details
- Use the attached photoshop template for bleed, sizing and fold lines
- final files must include a print ready PDF and fully editable PSD (photoshop) file with included fonts.
Attached are the following files:
Contact details are:
Name: Tom Hadley
Tel: 0498 316 207
email: tom@tidewellestatesagency.com.au
Office: Level 3, 17 Carrow Rd, Merrigal NSW 2109
Web: www.tidewellestatesagency.com.au
Target Market(s)
35-75yo Male and Females that own investment properties on Sydney's Norther Beaches
Industry/Entity Type
Real Estate
Requirements
Must have
- The flyer must:
- - Be double sided and colour
- - be designed to match our website www.tidewellestatesagency.com.au
- - Contain our logo and contact details
- - Use the attached photoshop template for bleed, sizing and fold lines
- - final files must include a print ready PDF and fully editable PSD (photoshop) file with included fonts.
Nice to have
- A Money back guarantee "stamp"

```html
<!DOCTYPE html>
<html lang="en">
<head>
<meta charset="utf-8">
<title>Tidewell Estates Agency – Trifold Flyer</title>
<link href="https://fonts.googleapis.com/css2?family=Open+Sans:wght@400;600;700&display=swap" rel="stylesheet">
<style>
  :root {
    --page-bg: #eceef0;
    --teal-box: rgba(22, 88, 106, 0.92);
    --teal-heading: #41c3c9;
    --navy: #1f4f66;
    --ink: #2b2f36;
    --footer: #2f3a4b;
    --white: #ffffff;
    --sky: #8fd0e8;
    --sky-deep: #3fa9d4;
    --house: #2c3a44;
    --foliage: #4f7a4a;
  }
  * { box-sizing: border-box; margin: 0; padding: 0; }
  html, body {
    width: 1200px; height: 944px; overflow: hidden;
    background: var(--page-bg);
    font-family: "Open Sans", Arial, sans-serif;
  }
  .trifold {
    position: absolute; left: 45px; top: 42px;
    width: 1110px; height: 860px;
    display: flex;
    box-shadow: 0 6px 24px rgba(0,0,0,0.15);
  }
  .panel { position: relative; width: 370px; height: 860px; overflow: hidden; }

  /* Inside panel */
  .panel--inside .photo {
    position: absolute; inset: 0;
    background:
      linear-gradient(180deg, #d8eef6 0%, var(--sky) 6%, #3d4a52 14%, var(--house) 40%, #58745a 62%, var(--foliage) 78%, #a9c39a 100%);
  }
  .info-box {
    position: absolute; left: 48px; top: 110px; width: 290px; height: 612px;
    background: var(--teal-box);
    border: 2px solid rgba(255,255,255,0.85);
    padding: 22px 20px;
    color: var(--white);
    font-size: 11.6px; line-height: 1.38;
  }
  .info-box h2 {
    font-size: 16px; font-weight: 400; letter-spacing: 0.5px;
    color: var(--teal-heading); text-transform: uppercase;
    margin-bottom: 8px;
  }
  .info-box p { margin-bottom: 14px; }

  /* Cover contact panel */
  .panel--contact { background: var(--white); }
  .panel--contact .photo {
    position: absolute; left: 0; top: 0; width: 100%; height: 720px;
    background:
      linear-gradient(180deg, var(--sky-deep) 0%, #bfe5f2 8%, #ffffff 16%, #ffffff 20%, #6a7580 28%, #3b4852 42%, #5b7d5e 58%, #8fae88 68%, #dfe8dd 78%, #ffffff 86%);
  }
  .brand {
    position: absolute; left: 0; right: 0;
    text-align: center; font-weight: 700; letter-spacing: 0.5px;
    text-transform: uppercase;
  }
  .panel--contact .brand { top: 78px; font-size: 19px; color: var(--ink); }
  .contact {
    position: absolute; left: 0; right: 0; top: 742px;
    text-align: center; color: var(--ink);
  }
  .contact__name { font-size: 15px; font-weight: 700; color: var(--navy); letter-spacing: 0.5px; }
  .contact__phone { font-size: 22px; font-weight: 400; margin: 2px 0 4px; }
  .contact__line { font-size: 11px; line-height: 1.35; }
  .web-band {
    position: absolute; left: 0; right: 0; bottom: 0; height: 52px;
    background: var(--footer); color: var(--white);
    display: flex; align-items: center; justify-content: center;
    font-size: 12.5px;
  }
  /* contact block sits above band: shift */
  .panel--contact .contact { top: 690px; }

  /* Front panel */
  .panel--front .photo {
    position: absolute; inset: 0;
    background:
      linear-gradient(180deg, var(--sky-deep) 0%, #6cc2e2 22%, #b9e2f0 34%, #5f7076 44%, #33505a 58%, #1f5560 74%, #1b4e5a 100%);
  }
  .panel--front .brand { top: 88px; font-size: 22px; color: var(--white); }
  .headline {
    position: absolute; left: 30px; top: 380px; right: 20px;
    color: var(--white); font-size: 46px; font-weight: 600;
    line-height: 1.0; text-transform: uppercase; letter-spacing: 0.5px;
  }
  .front-copy {
    position: absolute; left: 30px; right: 24px; top: 672px;
    color: var(--white); font-size: 12px; line-height: 1.42;
  }
  .front-copy p { margin-bottom: 10px; }
</style>
</head>
<body>
  <main class="trifold">
    <section class="panel panel--inside">
      <div class="photo" role="img" aria-label="Modern two-storey townhouses with balconies and landscaped garden stairs under a blue sky"></div>
      <div class="info-box">
        <h2>Retaining Great Tenants</h2>
        <p>Here at Tidewell Estates Agency we understand the value of quality tenants. They ensure your investment property is well looked after, rent is paid on time and make our jobs here much easier. We like to let quality tenants know that we appreciate them. From time to time we send out small rewards and gifts to thank them for being great, paying on time and looking after your property.</p>
        <p>Right now we are sending out a little Christmas gift and card to all our tenants. This is not something we charge landlords for, we just want to hold on to quality tenants and show them our appreciation.</p>
        <h2>Our Broad Team</h2>
        <p>Not only do we have a friendly, professional and efficient property management team – we also work closely with associated builders, accountants and mortgage brokers. So you have access to experienced professionals in all facets of property investment.</p>
        <p>We work for you and its in our best interest that you get the best advice and service possible to get the most out of your investment.</p>
      </div>
    </section>

    <section class="panel panel--contact">
      <div class="photo" role="img" aria-label="Contemporary townhouse facade with slatted balcony screens and lush garden steps"></div>
      <div class="brand">Tidewell Estates Agency</div>
      <div class="contact">
        <div class="contact__name">TOM HADLEY</div>
        <div class="contact__phone">0498 316 207</div>
        <div class="contact__line">email: tom@tidewellestatesagency.com.au</div>
        <div class="contact__line">Office: Level 3, 17 Carrow Rd,</div>
        <div class="contact__line">Merrigal NSW 2109</div>
      </div>
      <div class="web-band">www.tidewellestatesagency.com.au</div>
    </section>

    <section class="panel panel--front">
      <div class="photo" role="img" aria-label="Row of modern townhouses with garden stairs beneath a bright sky with clouds"></div>
      <div class="brand">Tidewell Estates Agency</div>
      <h1 class="headline">What<br>Separates<br>Tidewell<br>Estates<br>Agency</h1>
      <div class="front-copy">
        <p>Tidewell Estates Agency is a boutique agency that specializes in Property Management.</p>
        <p>We differ from your typical agency because our primary business is property management. You will have a senior property manager that is solely focused on maximizing your investments potential. As property investors ourselves we understand the frustrations you have with a typical agency, and we promise to offer you the service, care and professionalism beyond what you expect. Guaranteed!</p>
      </div>
    </section>
  </main>
</body>
</html>
```